Health & Fitness Author & Public Speaker Needs Visually Stunning Web Design!

We've FINALLY got around to launching a website for Belinda Marchetti - Australian Food Coach and Health & Fitness Expert. The website is to promote her new healthy eating program - "Bright Plate Living".
For a compehensive outline of exactly what we are after, please see the following attached files:
(1) Web Layout (wireframe, content/copy, links to photos to use, sample page we love)
(2) Style Guide (these are the colours, and overall feel we want)
Photos that we'd like used (of Belinda, and food/meals) can be found at these URL's:
Profile: https://www.filecrate.example/sh/q4r8vpl2m7xz/K3tPzWq9Lm
PicVault: https://www.filecrate.example/sh/b7nwe3ju1kd5/9hFrTy2Qxa
HINT:
Before you do ANYTHING - check out this site as it is pretty much EXACTLY what we're after, but with our branding/colours/style: http://tessamorrow.example/
As we will need to revamp our existing Chatterbook page & other printed material, there may be the potential for further work for the successful designer in the future.
Thanks & Good Luck!
Donovan Pryle
Marketing & Business Development Manager
Bright Plate Living
Women, Ages 24 - 45, Interested in Healthly Eating & Fitness
Business

```html
<!DOCTYPE html>
<html lang="en">
<head>
<meta charset="utf-8">
<title>Bright Plate Living</title>
<link href="https://fonts.googleapis.com/css2?family=Questrial&family=Montserrat:ital,wght@0,500;1,500&display=swap" rel="stylesheet">
<style>
:root{
  --pink:#ea1660;
  --magenta:#b5128a;
  --purple:#8a4bbf;
  --purple-dark:#7436ad;
  --ink:#333;
  --muted:#b7b7b7;
  --dark:#2a2a2c;
  --footer:#3b3c41;
  --page:#ffffff;
  --frame:#e8e8e8;
}
*{box-sizing:border-box;margin:0;padding:0}
html,body{width:960px;height:1200px;overflow:hidden}
body{background:var(--frame);font-family:"Questrial",sans-serif;color:var(--ink);position:relative}
.abs{position:absolute}
.page{position:absolute;left:24px;top:0;width:912px;height:1200px;background:var(--page)}
.logo{left:84px;top:42px;font-size:19px;color:var(--pink);letter-spacing:-.2px}
.nav a{position:absolute;top:45px;height:22px;line-height:22px;font-size:12px;color:#111;text-decoration:none;text-transform:uppercase}
.nav .active{background:var(--pink);color:#fff;border-radius:2px;padding:0 13px}
.hero{left:24px;top:80px;width:912px;height:426px;background:radial-gradient(ellipse at 25% 45%,#7e6f66 0%,#55524f 40%,#3a3a3a 75%,#2c2c2c 100%)}
.hero-photo{left:24px;top:80px;width:390px;height:426px;background:linear-gradient(180deg,#6a5a52 0%,#8c7468 50%,#4c443f 100%);opacity:.55}
.hero-head{left:468px;font-family:"Montserrat",sans-serif;font-weight:500;color:#fff;text-transform:uppercase;line-height:1}
.h1{font-size:45px;letter-spacing:.5px}
.h1 small{font-size:15px;letter-spacing:.5px}
.hero-sub{left:467px;top:327px;font-family:"Montserrat",sans-serif;font-weight:500;color:#fff;font-size:24px}
.hero-by{left:468px;top:362px;font-family:"Montserrat",sans-serif;font-style:italic;font-weight:500;color:var(--pink);font-size:15px}
.band{left:24px;top:506px;width:912px;height:72px;background:var(--pink)}
.band-title{left:94px;top:518px;font-size:18px;color:#7a0e35;letter-spacing:-.3px}
.band-text{left:94px;top:538px;font-size:11px;color:#fff;line-height:13px;text-transform:uppercase}
.field{background:#fff;border:1px solid #ddd;font-size:9px;color:#aaa;padding:0 8px;display:flex;align-items:center;border-radius:2px}
.btn-dark{background:linear-gradient(#3a3a3a,#151515);color:#fff;border-radius:3px;display:flex;align-items:center;justify-content:center}
.post-title{left:84px;width:490px;font-size:21px;letter-spacing:-.8px;line-height:25px;color:#333}
.meta{font-size:10.5px;color:var(--magenta);display:flex;align-items:center}
.meta svg{margin-right:8px}
.thumb{left:84px;width:180px;height:94px}
.excerpt{left:279px;width:292px;font-size:10.4px;line-height:14.5px;color:var(--muted)}
.divider{left:80px;top:866px;width:490px;height:1px;background:#ececec}
.card{border:1px solid #e2e2e2}
.guide{left:600px;top:606px;width:277px;height:164px;background:#f3f3f3}
.guide-title{left:614px;top:641px;font-size:19px;line-height:18px;letter-spacing:-.8px;color:#333}
.book{left:764px;top:624px;width:96px;height:120px;background:linear-gradient(160deg,#fafafa 0%,#eeeaf0 45%,#e14f95 75%,#a0367e 100%);box-shadow:2px 2px 4px rgba(0,0,0,.25)}
.challenge{left:600px;top:792px;width:277px;height:171px;background:linear-gradient(90deg,#d8d4cf 0%,#eeebe7 60%,#f4f2ef 100%)}
.challenge-photo{left:601px;top:793px;width:125px;height:169px;background:linear-gradient(180deg,#9d8e84 0%,#b9aba2 45%,#8d8a8e 100%)}
.challenge-title{right:94px;top:819px;font-size:15px;letter-spacing:-.8px;color:#333}
.challenge-text{right:94px;top:850px;font-size:15px;line-height:19px;letter-spacing:-.6px;color:var(--magenta);text-align:center}
.join{left:600px;top:986px;width:277px;height:133px;background:linear-gradient(135deg,#a56ccd 0%,var(--purple) 55%,var(--purple-dark) 100%);border:1px solid #6c2ea2}
.join-title{left:615px;top:993px;font-size:19px;color:#2a1538}
.join-text{left:615px;top:1020px;width:255px;font-size:10.5px;line-height:13px;color:#f3e9fb}
.btn-light{background:linear-gradient(#f4f4f4,#d6d6d6);color:#222;border-radius:3px;display:flex;align-items:center;justify-content:center;font-size:10px}
.footer{left:24px;top:1142px;width:912px;height:58px;background:var(--footer)}
.foot-link{top:1163px;font-size:11.5px;color:#fff}
.social-label{left:734px;top:1150px;font-size:11px;color:#fff;text-transform:uppercase}
.social{top:1170px;width:18px;height:18px;border-radius:2px}
</style>
</head>
<body>
<div class="page"></div>

<header>
  <div class="abs logo">Bright Plate Living</div>
  <nav class="nav">
    <a class="active" style="left:553px">Home</a>
    <a style="left:642px">About</a>
    <a style="left:724px">The Plan</a>
    <a style="left:820px">Shop</a>
  </nav>
</header>

<section>
  <div class="abs hero"></div>
  <div class="abs hero-photo" role="img" aria-label="Portrait of Belinda Marchetti holding a bunch of green grapes against a weathered stone wall"></div>
  <div class="abs hero-head h1" style="top:170px">Get Slim</div>
  <div class="abs hero-head h1" style="top:217px">Boost Energy</div>
  <div class="abs hero-head h1" style="top:265px">Guilt Free <small>with</small></div>
  <div class="abs hero-sub">BRIGHT PLATE LIVING!</div>
  <div class="abs hero-by">WITH BELINDA MARCHETTI</div>
</section>

<section>
  <div class="abs band"></div>
  <div class="abs band-title">Join the BRIGHT PLATE LIVING Movement !</div>
  <div class="abs band-text">Get &nbsp;a weekly serving of love &amp; wisdom that will<br>change your life...bring it on</div>
  <div class="abs field" style="left:509px;top:529px;width:135px;height:25px">Your Name</div>
  <div class="abs field" style="left:652px;top:529px;width:134px;height:25px">Your Email</div>
  <div class="abs btn-dark" style="left:792px;top:529px;width:84px;height:25px;font-size:9.5px">Hook Me Up</div>
</section>

<main>
  <article>
    <h2 class="abs post-title" style="top:613px">A Year In Review: Gratitude, Thoughts, Reflections, and Revelation</h2>
    <div class="abs meta" style="left:84px;top:677px">By: Admin</div>
    <div class="abs meta" style="left:152px;top:677px"><svg width="13" height="12"><rect x="1" y="2" width="11" height="9" rx="2" fill="none" stroke="#c98a3a" stroke-width="1.5"/></svg>January 17, 2013</div>
    <div class="abs meta" style="left:274px;top:677px"><svg width="13" height="12"><path d="M1 5h4l6-3v8l-6-3H1z" fill="#d24b3a"/></svg>Related Blogs</div>
    <div class="abs meta" style="left:386px;top:677px"><svg width="13" height="12"><ellipse cx="6" cy="6" rx="5" ry="4" fill="#cfe3f0" stroke="#7aa7c2"/><circle cx="10" cy="9" r="2.5" fill="#4bb54b"/></svg>No comments</div>
    <div class="abs thumb" style="top:712px;background:linear-gradient(90deg,#c9d4dc 0%,#e8e2dc 45%,#d9a27c 70%,#efe9ef 100%)" role="img" aria-label="Group of smiling people on exercise bikes in a spin class"></div>
    <p class="abs excerpt" style="top:710px">Contrary to popular belief, Lorem Ipsum is not simply random text. It has roots in a piece of classical Latin literature from 45 BC, making it over 2000 years old. Harold Penwick, a Latin professor at Ashbury Hill College in Virginia, looked up one of the more obscure Latin words, consectetur, from a Lorem Ipsum passage, and going through the cites of the.</p>
    <div class="abs btn-dark" style="left:84px;top:827px;width:87px;height:24px;font-size:12px">Get It Now</div>
  </article>

  <div class="abs divider"></div>

  <article>
    <h2 class="abs post-title" style="top:880px">Habit Creation: Using Technology To Reach Your Fitness Goals</h2>
    <div class="abs meta" style="left:84px;top:941px">By: Admin</div>
    <div class="abs meta" style="left:152px;top:941px"><svg width="13" height="12"><rect x="1" y="2" width="11" height="9" rx="2" fill="none" stroke="#c98a3a" stroke-width="1.5"/></svg>January 17, 2013</div>
    <div class="abs meta" style="left:274px;top:941px"><svg width="13" height="12"><path d="M1 5h4l6-3v8l-6-3H1z" fill="#d24b3a"/></svg>Related Blogs</div>
    <div class="abs meta" style="left:388px;top:941px"><svg width="13" height="12"><ellipse cx="6" cy="6" rx="5" ry="4" fill="#cfe3f0" stroke="#7aa7c2"/><circle cx="10" cy="9" r="2.5" fill="#4bb54b"/></svg>No comments</div>
    <div class="abs thumb" style="top:976px;background:linear-gradient(90deg,#3a3a3a 0%,#c98f66 45%,#e4c08f 75%,#c88a4f 100%)" role="img" aria-label="Smiling woman doing sit-ups in a group fitness class"></div>
    <p class="abs excerpt" style="top:973px">Contrary to popular belief, Lorem Ipsum is not simply random text. It has roots in a piece of classical Latin literature from 45 BC, making it over 2000 years old. Harold Penwick, a Latin professor at Ashbury Hill College in Virginia, looked up one of the more obscure Latin words, consectetur, from a Lorem Ipsum passage, and going through the.</p>
    <div class="abs btn-dark" style="left:84px;top:1090px;width:87px;height:24px;font-size:12px">Get It Now</div>
  </article>
</main>

<aside>
  <div class="abs card guide"></div>
  <div class="abs guide-title">The Ultimate Bright<br>Plate Living<br>Guide</div>
  <div class="abs book" role="img" aria-label="Cover of The Bright Plate Living eating plan book with a bowl of berries"></div>
  <div class="abs btn-dark" style="left:617px;top:715px;width:94px;height:28px;font-size:12px">Get It Now</div>

  <div class="abs card challenge"></div>
  <div class="abs challenge-photo" role="img" aria-label="Belinda Marchetti smiling and carrying a rolled yoga mat"></div>
  <div class="abs challenge-title">12 WEEK CHALLENGE</div>
  <div class="abs challenge-text">Healthy, Happy &amp;<br>Hot In No Time Flat!</div>
  <div class="abs btn-dark" style="left:766px;top:919px;width:75px;height:23px;font-size:10px">Join Me Up</div>

  <div class="abs join"></div>
  <div class="abs join-title">Join the Movement !</div>
  <p class="abs join-text">Join the Bright Plate Living Movement and get a free copy of The Kick Start Plan (valued $27.00)</p>
  <div class="abs field" style="left:615px;top:1056px;width:121px;height:22px">Your Name</div>
  <div class="abs field" style="left:743px;top:1056px;width:121px;height:22px">Your Email</div>
  <div class="abs btn-light" style="left:616px;top:1086px;width:75px;height:22px">Sign Me Up</div>
</aside>

<footer>
  <div class="abs footer"></div>
  <div class="abs foot-link" style="left:84px">Community</div>
  <div class="abs foot-link" style="left:160px">Free Resources</div>
  <div class="abs foot-link" style="left:254px">Press</div>
  <div class="abs foot-link" style="left:300px">Contact</div>
  <div class="abs social-label">Social Media Buttons:</div>
  <div class="abs social" style="left:735px;background:#3b5b9a"></div>
  <div class="abs social" style="left:761px;background:#3fa8e0"></div>
  <div class="abs social" style="left:787px;background:#c8261f"></div>
</footer>
</body>
</html>
```